Surgical Conditions of the thyroid and parathyroid glands - a flyer for GPs

Hi there,

I am a thyroid surgeon trying to produce a bi-fold A4 flyer as a quick reference guide for general practitioners (family doctors). It needs to feel friendly and professional.

The text for the four "pages" can be found in the "thyroid flyer for design" document attached.

The front page should have:
- The title
- the photo with the patient having an ultrasound
- the photo of the asian woman with the enlarged thyroid gland
- possibly the photo of the blonde woman touching her neck

The inner two pages are predominantly text - I would love this to be presented in an easy to read, uncluttered format. There is a photo attached which demonstrates the parathyroid glands. This should be placed near the parathyroid text section if possible.

The back page is a brief bio of myself. It should have the profile pic attached.
It should have contact details, which I forgot to put in the word document. These details are:
Phone (03) 9482 5170 for all appointments
Consulting at:
18 Wattlebird Lane, Berwick, VIC 3806
hollowaymedicalteam.com.au
dorianpelsworth.com

The back page should also have the "Tarrow Care" and "Guild of Operators" logos.

If possible, all pages should have the "Holloway Medical Team" logo.

The whole feel could have a similar colour scheme to my group website (largely orange and green). Please see www.hollowaymedicalteam.com.au for examples.

Many thanks!

Target Market(s)

General practitioners (ie family doctors)

Industry/Entity Type

Medical And Science

Font styles to use
Sans Serif

Colors
33b8a4
f78f20

Requirements
Must have
• Contact details on the back, holloway medical team logo on front and back pages, Tarrow Care and Guild of Operators logo on the back.
Nice to have
• Other medical/surgical related images as you see fit - sorry to be so broad!!

```html
<!DOCTYPE html>
<html lang="en">
<head>
<meta charset="utf-8">
<title>Thyroid &amp; Parathyroid – GP Quick Reference</title>
<link href="https://fonts.googleapis.com/css2?family=Exo+2:wght@600;700&family=Fira+Sans:wght@300;400&display=swap" rel="stylesheet">
<style>
  :root{
    --green:#1e9b78;
    --orange:#ec6a0c;
    --orange-text:#e8670a;
    --ink:#2a2a2a;
    --white:#ffffff;
    --fold:#e4e4e4;
  }
  *{margin:0;padding:0;box-sizing:border-box}
  html,body{width:1200px;height:865px;overflow:hidden;background:var(--white)}
  .spread{position:relative;width:1200px;height:865px;overflow:hidden;font-family:"Fira Sans",sans-serif;color:var(--ink)}
  .backdrop{position:absolute;inset:0}
  .fold{position:absolute;left:590px;top:0;width:1px;height:865px;background:var(--fold)}
  .photo{position:absolute;border-radius:50%;border:5px solid var(--white);box-shadow:0 0 0 1px #ddd}
  .photo-neck{left:60px;top:35px;width:104px;height:104px;background:radial-gradient(circle at 40% 40%,#a8724f,#6e4430 70%,#c98c96)}
  .photo-glands{left:1031px;top:663px;width:132px;height:132px;background:radial-gradient(circle at 50% 55%,#f0f0f0,#cfcfcf 75%,#bdbdbd)}
  .bar{position:absolute;height:36px;background:var(--orange);border-radius:0 18px 18px 0;color:var(--white);font-family:"Exo 2",sans-serif;font-weight:700;font-size:22.5px;line-height:36px;padding-left:18px;letter-spacing:.2px}
  .bar-common{left:102px;top:149px;width:453px}
  .bar-symptoms{left:102px;top:541px;width:453px}
  .bar-workup{left:610px;top:147px;width:387px;border-radius:6px 18px 18px 6px;padding-left:10px}
  .bar-para{left:611px;top:655px;width:387px;border-radius:6px 18px 18px 6px;padding-left:10px}
  .condition{position:absolute;left:102px;width:453px}
  .condition h3{font-weight:400;font-size:15px;color:var(--orange-text);line-height:17px}
  .condition p{font-weight:300;font-size:12.8px;line-height:14.5px;text-align:justify}
  .symptom-list{position:absolute;font-size:12.8px;font-weight:300;line-height:17.5px}
  .symptom-list h4{font-weight:400;font-size:13.2px;color:var(--orange-text);line-height:17px;margin-bottom:1px}
  .symptom-list ul{list-style:none}
  .symptom-list li::before{content:"•";color:var(--orange-text);margin-right:3px}
  .workup{position:absolute;left:609px;width:445px;font-weight:300;font-size:12.8px;line-height:16.4px}
  .workup .q{margin-top:16px}
  .workup h3{font-weight:400;font-size:15px;color:var(--orange-text);line-height:17px}
  .workup ul{list-style:none;padding-left:18px}
  .workup li{position:relative;line-height:17.4px}
  .workup li::before{content:"•";color:var(--orange-text);position:absolute;left:-18px}
  .para-text{position:absolute;left:609px;top:705px;width:410px;font-weight:300;font-size:12.8px;line-height:16.4px}
</style>
</head>
<body>
<div class="spread">
  <svg class="backdrop" width="1200" height="865" viewBox="0 0 1200 865" aria-hidden="true">
    <path d="M0 0 H166 C118 60 84 150 80 300 C76 500 70 700 74 865 H0 Z" fill="var(--green)"/>
    <path d="M92 150 Q40 470 76 865 H98 Q58 470 100 148 Z" fill="var(--orange)"/>
    <path d="M985 0 H1200 V865 H1178 Q1170 330 985 0 Z" fill="var(--green)"/>
    <path d="M940 0 H968 Q1168 300 1172 865 H1156 Q1148 340 940 0 Z" fill="var(--orange)"/>
  </svg>
  <div class="fold"></div>

  <div class="photo photo-neck" role="img" aria-label="Photo of a patient's neck showing an enlarged thyroid gland"></div>
  <div class="photo photo-glands" role="img" aria-label="Illustration of the thyroid with four highlighted parathyroid glands"></div>

  <div class="bar bar-common">Common thyroid disorders</div>

  <div class="condition" style="top:198px"><h3>Solitary nodules</h3><p>Often require characterisation with ultrasound +/- fine needle aspirate to determine likelihood of malignancy</p></div>
  <div class="condition" style="top:255px"><h3>Multinodular goitre</h3><p>Usually benign but may cause compressive symptoms</p></div>
  <div class="condition" style="top:298px"><h3>Graves’ disease</h3><p>Autoimmune stimulation of TSH receptors leading to hyperthyroidism</p></div>
  <div class="condition" style="top:341px"><h3>Thyroid cancer</h3><p style="text-align:left">Important risk factors include family history and a history of radiation exposure. Readily treatable with surgery, often in conjunction with radioactive iodine</p></div>
  <div class="condition" style="top:413px"><h3>Hashimoto’s thyroiditis</h3><p>Usually self-limiting, can cause hyperthyroidism (early) or hypothyroidism (late). May benefit from surgery if associated with ongoing pain</p></div>
  <div class="condition" style="top:470px"><h3>Thyroglossal cyst</h3><p>Presents as a midline lump above the thyroid cartilage (Adam’s apple), may become inflamed or form fistulas to the overlying skin</p></div>

  <div class="bar bar-symptoms">Common symptoms of thyroid disease</div>

  <div class="symptom-list" style="left:102px;top:589px">
    <h4>Symptoms of hyperthyroidism</h4>
    <ul><li>Tiredness</li><li>Palpitations</li><li>Tremor</li><li>Sweats</li><li>Heat intolerance</li><li>Exophthalmos</li><li>Diarrhoea</li><li>Weight loss</li><li>Menorrhagia</li></ul>
  </div>
  <div class="symptom-list" style="left:316px;top:589px">
    <h4>Symptoms of hypothyroidism</h4>
    <ul><li>Lethargy</li><li>Weight gain</li><li>Weakness</li><li>Cold</li><li>Hair loss</li></ul>
  </div>
  <div class="symptom-list" style="left:316px;top:708px">
    <h4>Compressive symptoms</h4>
    <ul><li>Lump in the neck</li><li>Dysphagia</li><li>Dyspnoea</li><li>Voice change</li></ul>
  </div>

  <div class="bar bar-workup">Workup for thyroid disorders</div>

  <div class="workup" style="top:198px">
    <p>Most thyroid disorders requiring surgical intervention can be diagnosed with athyroid ultrasound and thyroid function tests. If a patient is biochemically hyperthyroid, a thyroid nuclear scanand anti-TSH receptor antibodies are useful to determine the underlying cause (eg Graves’ disease, toxic nodule or toxic goitre). Thyroid antibodies can also determine if there is underlying thyroiditis. All patients with thyroid disease should also undergo screening for concurrent parathyroid disease with PTH,calcium and vitamin D levels. A nodule with suspicious features on ultrasound (increased vascularity, microcalcifications, irregular border) should undergo ultrasound-guided fine needle aspirate.</p>
    <p class="q">Which nodules should undergo fine needle aspirate?</p>
    <h3>Nodules &lt;1 cm</h3>
    <ul>
      <li>If there are suspicious features on ultrasound (irregular border, microcalcifications, increased vascularity)</li>
      <li>Nodules without suspicious features less than 1 cm can be re-evaluated with an ultrasound in 1 year</li>
    </ul>
    <h3>Nodules 1 to 3 cm</h3>
    <ul><li>Should undergo FNA, especially if there are suspicious features</li></ul>
    <h3>Nodules &gt;3cm</h3>
    <ul>
      <li>Should undergo FNA</li>
      <li>These nodules are more likely to become symptomatic and there is an increased risk of a false negative FNA with nodules of this size. They should therefore be considered for excision via a hemithyroid ectomy. An FNA can determine if a total thyroidectomy is preferred in the case of malignancy.</li>
    </ul>
  </div>

  <div class="bar bar-para">Parathyroid disease</div>

  <p class="para-text">Simple screening with calcium and PTH levels can detect hyperparathyroidism before symptoms become evident. Patients with osteoporosis, recurrent kidney stones or pathological fractures should be tested, as well as with an ultrasound to look for concurrent thyroid issues.</p>
</div>
</body>
</html>
```